Create two Wordpress Templates for a Coffee Startup

I'm looking for 2 templates.

One that will act as an under construction page until we launch and the other will be for when we launch.

UNDER CONSTRUCTION PAGE:
Simple doesn't have to be anymore than a landing page/splash page.
I'd like a countdown till launch start page that counts down from 1million. 1 Million cups till launch.
Mailchimp email subscriber signup to learn more/ stay up to date.
Video loop in background of a cup of coffee being poured.

TEMPLATE FOR LAUNCH:
I've attatched some .jpg files of an idea to go off and I'm fond of the [login to view URL] page.

```html
<!DOCTYPE html>
<html lang="en">
<head>
<meta charset="utf-8">
<title>Brewline – Everything You Love About Coffee</title>
<link rel="stylesheet" href="https://fonts.googleapis.com/css2?family=Questrial&family=Mulish:wght@600;700&display=swap">
<style>
  :root {
    --navy: #0c2a7e;
    --orange: #e57a2e;
    --button-blue: #1f6fb4;
    --button-text: #2266a8;
    --ink: #4a4a4a;
    --muted: #5c5c5c;
    --footer-text: #b9c3e0;
    --white: #ffffff;
    --band: #f1f0f0;
  }
  * { margin: 0; padding: 0; box-sizing: border-box; }
  html, body { width: 848px; height: 1200px; overflow: hidden; background: var(--white); }
  body { position: relative; font-family: "Questrial", sans-serif; color: var(--ink); }
  .abs { position: absolute; }

  /* Header */
  .site-header { left: 0; top: 0; width: 848px; height: 56px; background: var(--navy); }
  .nav-link {
    position: absolute; top: 33px; height: 22px; background: var(--white);
    border-radius: 2px; color: var(--button-text); font-size: 11.5px;
    display: flex; align-items: center; justify-content: center;
  }
  .nav-link.is-active { background: var(--orange); color: var(--white); border: 1px solid #f3a565; }
  .brand { left: 346px; top: 4px; height: 40px; display: flex; align-items: center; gap: 10px; }
  .brand-mark { width: 22px; height: 22px; background: var(--orange); }
  .brand-name { font-size: 23px; color: var(--white); letter-spacing: 1.5px; }

  /* Hero */
  .hero {
    left: 0; top: 56px; width: 848px; height: 213px;
    background: radial-gradient(ellipse at 50% 45%, #f0c7ab 0%, #d8956a 45%, #9c4f2a 80%, #6e3318 100%);
  }
  .hero-title {
    left: 0; top: 120px; width: 848px; text-align: center;
    font-family: "Mulish", sans-serif; font-weight: 700; font-size: 26px; color: var(--white);
  }
  .hero-tagline { left: 0; top: 173px; width: 848px; text-align: center; font-size: 17.5px; color: var(--white); letter-spacing: .3px; }
  .btn {
    position: absolute; background: var(--button-blue); color: var(--white);
    font-size: 11.5px; border-radius: 2px; display: flex; align-items: center; justify-content: center;
  }

  /* Our coffee */
  .coffee-band { left: 0; top: 269px; width: 848px; height: 293px; background: linear-gradient(90deg, #e7e5e4 0%, var(--band) 15%, #f7f6f6 50%, var(--band) 85%, #e5e4e4 100%); }
  .section-title { font-family: "Mulish", sans-serif; font-weight: 700; font-size: 13.5px; color: #555; }
  .body-copy { font-size: 10.6px; line-height: 14px; color: var(--muted); }
  .photo { position: absolute; }
  .photo-cup { left: 462px; top: 276px; width: 254px; height: 160px; background: linear-gradient(135deg, #3a2418 0%, #7b5a44 40%, #e8e2da 55%, #2c1b12 100%); }
  .photo-espresso { left: 126px; top: 392px; width: 328px; height: 273px; background: linear-gradient(160deg, #2a1d14 0%, #8a7460 40%, #c9b9a3 60%, #4a3322 100%); }

  /* Story callout */
  .story { left: 126px; top: 681px; width: 596px; height: 99px; background: var(--orange); border-radius: 7px; }
  .story-title { left: 126px; top: 699px; width: 596px; text-align: center; font-family: "Mulish", sans-serif; font-weight: 700; font-size: 13.5px; color: var(--navy); }
  .story-text { left: 126px; top: 729px; width: 596px; text-align: center; font-size: 10.6px; color: #2a2a2a; }

  /* Store map */
  .store-map { left: 126px; top: 822px; width: 597px; height: 253px; border: 1px solid #e59a6a; background: linear-gradient(160deg, #a9c8f2 0%, #eae6dc 35%, #e9e5da 65%, #b3cdf0 100%); }

  /* Footer */
  .site-footer { left: 0; top: 1087px; width: 848px; height: 113px; background: var(--navy); }
  .footer-title { font-family: "Mulish", sans-serif; font-weight: 600; font-size: 11px; color: var(--footer-text); }
  .footer-line { font-size: 11px; color: var(--footer-text); }
  .social { top: 1155px; width: 16px; height: 16px; border-radius: 50%; background: var(--footer-text); }
</style>
</head>
<body>

<header class="abs site-header">
  <a class="nav-link is-active" style="left:130px;width:52px;">Home</a>
  <a class="nav-link" style="left:189px;width:50px;">Menu</a>
  <a class="nav-link" style="left:246px;width:73px;">Our stores</a>
  <div class="abs brand"><span class="brand-mark"></span><span class="brand-name">Brewline</span></div>
  <a class="nav-link" style="left:528px;width:66px;">About us</a>
  <a class="nav-link" style="left:602px;width:49px;">News</a>
  <a class="nav-link" style="left:658px;width:73px;">Contact us</a>
</header>

<section>
  <div class="abs hero" role="img" aria-label="Close-up photograph of roasted coffee beans"></div>
  <h1 class="abs hero-title">Brewline</h1>
  <p class="abs hero-tagline">Everything You Love About Coffee.</p>
  <a class="btn" style="left:384px;top:211px;width:79px;height:26px;">Read more</a>
</section>

<section>
  <div class="abs coffee-band" role="img" aria-label="Faded coffee bean backdrop"></div>
  <h2 class="abs section-title" style="left:126px;top:295px;">Our Coffee</h2>
  <p class="abs body-copy" style="left:126px;top:325px;width:300px;text-align:justify;">Here at Brewline we deliver superior quality products. We accept only the highest-quality beans, and craft roast every batch to bring you the finest coffees.</p>
  <div class="photo photo-cup" role="img" aria-label="Photograph of a cappuccino cup with cinnamon sticks and coffee beans"></div>
  <div class="photo photo-espresso" role="img" aria-label="Photograph of an espresso machine pouring into two cups"></div>
  <p class="abs body-copy" style="left:471px;top:456px;width:238px;text-align:justify;">We aim to serve the best quality and most interesting varieties of coffees, teas, espresso drinks and accompaniments at all times to everyone.</p>
</section>

<section>
  <div class="abs story"></div>
  <h2 class="abs story-title">Story in every cup</h2>
  <p class="abs story-text">Tell us your story with Brewline. What do you love most of your favourite coffee?</p>
  <a class="btn" style="left:381px;top:747px;width:85px;height:25px;">Read Stories</a>
</section>

<section>
  <h2 class="abs section-title" style="left:126px;top:793px;">Find our stores</h2>
  <div class="abs store-map" role="img" aria-label="Map showing store locations"></div>
</section>

<footer class="abs site-footer"></footer>
<p class="abs footer-title" style="left:38px;top:1129px;">Find Us on</p>
<span class="abs social" style="left:39px;"></span>
<span class="abs social" style="left:60px;"></span>
<span class="abs social" style="left:81px;"></span>
<span class="abs social" style="left:103px;"></span>
<p class="abs footer-title" style="left:320px;top:1113px;">Opening hours</p>
<p class="abs footer-line" style="left:320px;top:1139px;">Mon - Fri 9:00-18:00</p>
<p class="abs footer-line" style="left:320px;top:1163px;">Sat - Sun 11:00-18:00</p>
<p class="abs footer-title" style="left:602px;top:1113px;">Contact us</p>
<p class="abs footer-line" style="left:602px;top:1139px;">14 Harbour Quay Road, Dublin 4</p>
<p class="abs footer-line" style="left:602px;top:1163px;">hello@brewline.ie</p>

</body>
</html>
```